Real Estate Business card design

Company Name: Tamarind Holdings, LLC
subtitle: We pay cash for houses!
Daniel Whitcombe
Managing Director
555-214-0963
Dan@TamarindHoldingsLLC.example
www.TamarindHoldingsLLC.example

We pay referral fees for Seller and Buyer leads.

Back:
We offer referral fees for Seller and Buyer leads that close.

Please contact Hal at 555-214-0963 with your referrals or to learn more about the referral program!

I am open to different color options but I am going for a classic, elegant, clean, and professional look. Please use logo as a reference.

Target Market(s)

People selling their homes and people in the market for buying homes.

Contact Information for Business Card

please see project description

Font styles to use
Serif
Sans Serif
Script

Requirements
Must have
• must have my logo in it
Nice to have
• I like cards that are split down the middle but please come up with a few mock ups. Open to any color scheme.

```html
<!DOCTYPE html>
<html lang="en">
<head>
<meta charset="utf-8">
<title>Tamarind Holdings, LLC – Business Card</title>
<link rel="stylesheet" href="https://fonts.googleapis.com/css2?family=Cinzel:wght@500;600&family=Montserrat:wght@400;500&display=swap">
<style>
  :root {
    --bg: #b9b9b9;
    --card: #ffffff;
    --navy: #434c5a;
    --gold: #c49a6c;
    --gold-line: #d8bf9f;
    --text: #2f3440;
    --muted: #f1f1f1;
  }
  * { box-sizing: border-box; margin: 0; padding: 0; }
  html, body { width: 1200px; height: 788px; overflow: hidden; }
  body {
    background: linear-gradient(160deg, #cfcfcf 0%, var(--bg) 55%, #a3a3a3 100%);
    font-family: "Montserrat", sans-serif;
    color: var(--text);
    position: relative;
  }
  .card {
    position: absolute;
    width: 540px;
    height: 309px;
    background: var(--card);
    border-radius: 22px;
    overflow: hidden;
    box-shadow: 0 14px 30px rgba(0,0,0,0.22);
  }
  /* Front */
  .card--front { left: 50px; top: 110px; }
  .brand {
    position: absolute;
    left: 34px; top: 96px;
    display: flex; align-items: center; gap: 12px;
  }
  .brand__mark { width: 16px; height: 16px; background: var(--gold); flex: none; }
  .brand__name {
    font-weight: 500; font-size: 24px; line-height: 1.15;
    color: var(--navy);
  }
  .divider {
    position: absolute; left: 262px; top: 38px;
    width: 1px; height: 182px; background: var(--gold-line);
  }
  .contact { position: absolute; left: 284px; top: 40px; right: 20px; }
  .contact__name {
    font-family: "Cinzel", serif; font-weight: 600; font-size: 23px;
    letter-spacing: 0.5px; color: var(--navy); line-height: 1.1;
  }
  .contact__name span { color: var(--gold); }
  .contact__title { font-size: 12.5px; margin-top: 4px; margin-bottom: 12px; }
  .contact__row {
    display: flex; align-items: center; gap: 7px;
    font-size: 11.5px; line-height: 1.75; white-space: nowrap;
  }
  .contact__row svg { width: 10px; height: 10px; flex: none; fill: var(--gold); }
  .contact__note { font-size: 11.5px; line-height: 1.45; margin-top: 4px; }
  .band {
    position: absolute; left: 0; right: 0; bottom: 0; height: 44px;
    background: var(--navy);
    border-top: 3px solid #fff;
    box-shadow: 0 -1px 0 var(--gold);
    display: flex; align-items: center; justify-content: flex-end;
    padding-right: 150px;
    color: #fff; font-weight: 500; font-size: 13px; letter-spacing: 0.3px;
  }
  /* Back */
  .card--back { left: 610px; top: 370px; }
  .back__square {
    position: absolute; left: 254px; top: 50px; width: 32px; height: 32px;
    background: var(--gold);
  }
  .back__text { position: absolute; left: 0; right: 0; top: 118px; text-align: center; }
  .back__headline { font-size: 23px; font-weight: 500; letter-spacing: 0.4px; }
  .back__sub { font-size: 13.5px; margin-top: 3px; }
  .back__rule { width: 330px; height: 1px; background: var(--gold-line); margin: 14px auto 12px; }
  .back__cta { font-size: 13px; line-height: 1.5; }
  .back__cta strong { font-weight: 500; font-size: 19px; }
</style>
</head>
<body>
  <section class="card card--front" aria-label="Business card front">
    <div class="brand">
      <div class="brand__mark"></div>
      <div class="brand__name">Tamarind<br>Holdings, LLC</div>
    </div>
    <div class="divider"></div>
    <div class="contact">
      <h1 class="contact__name">DANIEL <span>WHITCOMBE</span></h1>
      <p class="contact__title">Managing Director</p>
      <p class="contact__row">
        <svg viewBox="0 0 10 10"><path d="M2 0.5 L3.6 2.6 L2.8 3.6 C3.5 5 4.8 6.4 6.3 7.2 L7.4 6.4 L9.5 8 L8.4 9.6 C4.5 9.2 0.8 5.4 0.4 1.6 Z"/></svg>
        555-214-0963
      </p>
      <p class="contact__row">
        <svg viewBox="0 0 10 10"><path d="M0 2 H10 V8.5 H0 Z M0.6 2.4 L5 5.6 L9.4 2.4" stroke="#fff" stroke-width="0.8"/></svg>
        Dan@TamarindHoldingsLLC.example
      </p>
      <p class="contact__row">
        <svg viewBox="0 0 10 10"><circle cx="5" cy="5" r="4.6"/><path d="M0.6 5 H9.4 M5 0.4 C2.6 3 2.6 7 5 9.6 M5 0.4 C7.4 3 7.4 7 5 9.6" stroke="#fff" stroke-width="0.6" fill="none"/></svg>
        www.TamarindHoldingsLLC.example
      </p>
      <p class="contact__note">We pay referral fees<br>for Seller and Buyer leads.</p>
    </div>
    <div class="band">We pay cash for houses!</div>
  </section>

  <section class="card card--back" aria-label="Business card back">
    <div class="back__square"></div>
    <div class="back__text">
      <h2 class="back__headline">We offer referral fees</h2>
      <p class="back__sub">for Seller and Buyer leads that close.</p>
      <div class="back__rule"></div>
      <p class="back__cta">Please contact Hal at <strong>555-214-0963</strong><br>with your referrals or to learn more about the referral program!</p>
    </div>
  </section>
</body>
</html>
```